Email template for construction companies

Hello, I'm looking to build out an html email template for our email marketing. I'd like it to compliment our website, but not be an exact replication of it.

This template will be used in all of our email marketing campaigns. We provide financial support for construction companies, so it needs to express stability and confidence, but not the stuffiness of a traditional bank.

Target Market(s)

Construction companies (subcontractors specifically)

Industry/Entity Type

Construction Company

Font styles to use
Serif

Requirements
Must have
• Must compliment our website, but not be a replica.
Should not have
• Should not be an exact replica of our website.

```html
<!DOCTYPE html>
<html lang="en">
<head>
<meta charset="utf-8">
<title>TradeFund Partners — We Fund Contractors</title>
<link rel="stylesheet" href="https://fonts.googleapis.com/css2?family=Oswald:wght@500;700&family=Open+Sans:wght@400;600;700&display=swap">
<style>
  :root {
    --header-bg: #2b2d31;
    --footer-bg: #2f3237;
    --ink: #2a2c30;
    --panel: #e4e5e6;
    --panel-icon: #cfd1d3;
    --brand-blue: #1f4e8c;
    --white: #ffffff;
    --muted: #9ea2a8;
    --fine: #8a8d91;
    --link: #1f4e8c;
  }
  * { box-sizing: border-box; margin: 0; padding: 0; }
  html, body { width: 800px; height: 1200px; overflow: hidden; }
  body { font-family: "Open Sans", Arial, sans-serif; background: var(--white); color: var(--ink); }
  .canvas { width: 800px; height: 1200px; position: relative; }

  .site-header {
    height: 78px; background: var(--header-bg);
    display: flex; align-items: center; justify-content: space-between;
    padding: 0 34px 0 28px;
  }
  .brand { display: flex; align-items: center; gap: 10px; color: var(--white);
    font-family: "Open Sans", Arial, sans-serif; font-weight: 600; font-size: 23px; }
  .brand-dot { width: 32px; height: 32px; border-radius: 50%; background: var(--brand-blue); }
  .main-nav { display: flex; gap: 44px; }
  .main-nav a { color: #d9dadc; text-decoration: none; font-size: 14px; }

  .hero { height: 562px; position: relative; overflow: hidden; }
  .hero-photo {
    position: absolute; inset: 0;
    background:
      linear-gradient(180deg, rgba(20,30,45,0.15), rgba(20,30,45,0.35)),
      linear-gradient(100deg, #3d4f6a 0%, #7a8796 35%, #c9b79a 60%, #d8cbb4 78%, #8b95a0 100%);
  }
  .hero-content { position: absolute; inset: 0; display: flex; flex-direction: column; align-items: center; }
  .hero-title {
    margin-top: 196px; text-align: center; color: var(--white);
    font-family: "Oswald", Impact, sans-serif; font-weight: 700;
    font-size: 92px; line-height: 0.98; letter-spacing: 1px;
    text-shadow: 0 2px 8px rgba(0,0,0,0.35);
  }
  .apply-button {
    margin-top: 100px; padding: 8px 26px;
    background: var(--brand-blue); color: var(--white);
    border: 3px solid var(--white); outline: 2px solid var(--brand-blue);
    font-family: "Oswald", Impact, sans-serif; font-weight: 500; font-size: 27px; letter-spacing: 1.5px;
    text-decoration: none;
  }

  .benefits { height: 282px; background: var(--panel); text-align: center; padding-top: 40px; }
  .benefits-title { font-family: "Open Sans", Arial, sans-serif; font-weight: 700; font-size: 30px; color: var(--ink); }
  .benefits-divider { display: block; margin: 14px auto 0; }
  .benefit-list { display: flex; justify-content: center; gap: 140px; margin-top: 4px; list-style: none; }
  .benefit { width: 120px; display: flex; flex-direction: column; align-items: center; }
  .benefit-icon {
    width: 88px; height: 88px; border-radius: 50%; background: var(--white);
    border: 4px solid var(--panel-icon);
    display: flex; align-items: center; justify-content: center;
  }
  .benefit-label { margin-top: 18px; font-weight: 700; font-size: 27px; color: var(--ink); }

  .site-footer { height: 175px; background: var(--footer-bg); padding: 34px 28px 0; color: var(--muted); position: relative; }
  .footer-row { display: flex; justify-content: space-between; align-items: flex-start; }
  .contact-lead { font-size: 15px; color: #b9bcc1; }
  .contact-details { font-size: 15px; color: var(--white); font-weight: 600; margin-top: 2px; }
  .social-links { display: flex; gap: 20px; margin-top: 14px; }
  .social-links span { width: 22px; height: 22px; border-radius: 50%; background: #d9dadc; display: block; }
  .copyright { position: absolute; left: 0; right: 0; bottom: 14px; text-align: center; font-size: 10.5px; color: #868a90; }

  .fine-print { padding: 20px 28px; font-size: 10px; line-height: 1.45; color: var(--fine); }
  .fine-print a { color: var(--link); }
</style>
</head>
<body>
<div class="canvas">
  <header class="site-header">
    <div class="brand"><span class="brand-dot"></span>TradeFund Partners</div>
    <nav class="main-nav">
      <a href="#">Home</a><a href="#">About</a><a href="#">Contractors</a><a href="#">Suppliers</a>
    </nav>
  </header>

  <section class="hero">
    <div class="hero-photo" role="img" aria-label="Smiling construction worker in a blue hard hat with a colleague in a hi-vis vest at a building site"></div>
    <div class="hero-content">
      <h1 class="hero-title">WE FUND<br>CONTRACTORS</h1>
      <a class="apply-button" href="#">APPLY NOW</a>
    </div>
  </section>

  <section class="benefits">
    <h2 class="benefits-title">Why Apply For A Line Of Trade Credit?</h2>
    <svg class="benefits-divider" width="22" height="22" viewBox="0 0 22 22" aria-hidden="true">
      <circle cx="11" cy="11" r="10" fill="none" stroke="#1f4e8c" stroke-width="2"/>
      <circle cx="11" cy="11" r="5" fill="#1f4e8c"/>
    </svg>
    <ul class="benefit-list">
      <li class="benefit">
        <div class="benefit-icon">
          <svg width="40" height="44" viewBox="0 0 40 44" aria-hidden="true">
            <rect x="6" y="2" width="28" height="4" fill="#2a2c30"/>
            <rect x="6" y="38" width="28" height="4" fill="#2a2c30"/>
            <path d="M10 6 L30 6 L30 10 L22 22 L30 34 L30 38 L10 38 L10 34 L18 22 L10 10 Z" fill="none" stroke="#2a2c30" stroke-width="3"/>
            <path d="M13 36 L20 27 L27 36 Z" fill="#2a2c30"/>
          </svg>
        </div>
        <span class="benefit-label">Time</span>
      </li>
      <li class="benefit">
        <div class="benefit-icon">
          <svg width="48" height="32" viewBox="0 0 48 32" aria-hidden="true">
            <rect x="2" y="4" width="44" height="24" rx="2" fill="none" stroke="#2a2c30" stroke-width="3"/>
            <circle cx="24" cy="16" r="6" fill="#2a2c30"/>
            <circle cx="10" cy="16" r="2" fill="#2a2c30"/>
            <circle cx="38" cy="16" r="2" fill="#2a2c30"/>
          </svg>
        </div>
        <span class="benefit-label">Money</span>
      </li>
      <li class="benefit">
        <div class="benefit-icon">
          <svg width="40" height="40" viewBox="0 0 40 40" aria-hidden="true">
            <path d="M36 4 C26 4 18 10 13 20 L20 27 C30 22 36 14 36 4 Z" fill="#2a2c30"/>
            <path d="M13 20 L6 20 L11 14 L18 14 Z M20 27 L20 34 L26 29 L26 22 Z" fill="#2a2c30"/>
            <path d="M11 26 C7 28 5 32 4 36 C8 35 12 33 14 29 Z" fill="#2a2c30"/>
            <circle cx="27" cy="13" r="3" fill="#ffffff"/>
          </svg>
        </div>
        <span class="benefit-label">Growth</span>
      </li>
    </ul>
  </section>

  <footer class="site-footer">
    <div class="footer-row">
      <div>
        <p class="contact-lead">Please let us serve you. Contact us.</p>
        <p class="contact-details">info@tradefundpartners.com | +1 (555) 014-2290</p>
      </div>
      <div class="social-links" aria-label="Social links">
        <span></span><span></span><span></span><span></span><span></span>
      </div>
    </div>
    <p class="copyright">Copyright © 2016 TradeFund Partners. All Rights Reserved. Patents Pending.</p>
  </footer>

  <p class="fine-print">
    TradeFund Partners values its customers and respects their privacy. For more information about our privacy policy, please click on the following link: <a href="#">Privacy Policy</a><br>
    To remove yourself from our email list, please <a href="#">click here</a> to unsubscribe. Please note that it may take up to 10 days to process your request.
  </p>
</div>
</body>
</html>
```